Lounge Night Poster

We need an attractive poster for our new lounge/night club in San Francisco called Velvora Nightclub, promoting our new event, "Lantern Drift". We will have a live band and Asian singers performing during the night. It is like a lounge where people can chill and have a sip. It will open on July 21.

Industry/Entity Type

Club

```html
<!DOCTYPE html>
<html lang="en">
<head>
<meta charset="UTF-8">
<title>Velvora Nightclub presents Lantern Drift</title>
<link rel="stylesheet" href="https://fonts.googleapis.com/css2?family=Jura:wght@600;700&display=swap">
<style>
  :root {
    --ink: #f5f3f8;
    --band: #552a86;
    --band-edge: #9a8cc0;
    --night-top: #2c1c50;
    --night-mid: #3d2868;
    --neon-teal: rgba(90, 210, 170, 0.55);
    --neon-red: rgba(235, 70, 110, 0.5);
    --neon-gold: rgba(240, 190, 90, 0.4);
    --wall-red: rgba(200, 60, 90, 0.55);
    --sofa: rgba(236, 228, 222, 0.7);
    --floor: #7f6fbf;
    --floor-light: #a497d6;
  }
  * { margin: 0; padding: 0; box-sizing: border-box; }
  html, body {
    width: 905px;
    height: 1200px;
    overflow: hidden;
    background: var(--night-top);
  }
  .poster {
    position: relative;
    width: 905px;
    height: 1200px;
    overflow: hidden;
    font-family: "Jura", sans-serif;
    color: var(--ink);
  }
  .venue-photo {
    position: absolute;
    inset: 0;
    background:
      radial-gradient(ellipse 55% 4% at 30% 2%, rgba(200, 180, 240, 0.5), transparent 80%),
      radial-gradient(ellipse 40% 3% at 25% 27%, var(--neon-teal), transparent 80%),
      radial-gradient(ellipse 35% 3% at 70% 28%, var(--neon-gold), transparent 80%),
      radial-gradient(ellipse 45% 3% at 20% 34%, var(--neon-red), transparent 80%),
      radial-gradient(ellipse 30% 3% at 60% 33%, var(--neon-teal), transparent 80%),
      radial-gradient(ellipse 40% 3% at 15% 29%, var(--neon-teal), transparent 80%),
      radial-gradient(ellipse 25% 6% at 80% 38%, rgba(220, 220, 255, 0.45), transparent 80%),
      radial-gradient(ellipse 50% 7% at 55% 58%, var(--wall-red), transparent 80%),
      radial-gradient(ellipse 14% 8% at 5% 57%, var(--wall-red), transparent 80%),
      radial-gradient(ellipse 20% 14% at 17% 75%, var(--sofa), transparent 80%),
      radial-gradient(ellipse 20% 12% at 78% 72%, var(--sofa), transparent 80%),
      radial-gradient(ellipse 8% 10% at 50% 75%, rgba(230, 200, 150, 0.55), transparent 80%),
      radial-gradient(ellipse 15% 10% at 90% 93%, rgba(255, 200, 230, 0.35), transparent 80%),
      linear-gradient(180deg, var(--night-top) 0%, var(--night-mid) 22%, #3a2560 38%, #4b2d6e 52%, #5b3f8a 62%, var(--floor) 80%, var(--floor-light) 100%);
  }
  .headline {
    position: absolute;
    top: 158px;
    left: 0;
    width: 100%;
    text-align: center;
    font-size: 90px;
    font-weight: 700;
    line-height: 1;
    letter-spacing: 0.5px;
  }
  .presents {
    position: absolute;
    top: 364px;
    left: 0;
    width: 100%;
    text-align: center;
    font-size: 46px;
    font-weight: 700;
    line-height: 1;
  }
  .event-band {
    position: absolute;
    top: 493px;
    left: 0;
    width: 100%;
    height: 144px;
    background: var(--band);
    border-top: 5px solid var(--band-edge);
    border-bottom: 5px solid var(--band-edge);
    display: flex;
    align-items: center;
    justify-content: center;
  }
  .event-title {
    font-size: 104px;
    font-weight: 700;
    line-height: 1;
  }
  .event-date {
    position: absolute;
    top: 1112px;
    left: 0;
    width: 100%;
    text-align: center;
    font-size: 46px;
    font-weight: 700;
    line-height: 1;
  }
</style>
</head>
<body>
  <main class="poster">
    <div class="venue-photo" role="img" aria-label="Blurred photo of a nightclub lounge interior with neon light strips, speakers, white sofas and a low table"></div>
    <h1 class="headline">Velvora Nightclub</h1>
    <p class="presents">presents</p>
    <div class="event-band">
      <h2 class="event-title">Lantern Drift</h2>
    </div>
    <p class="event-date">July 21.</p>
  </main>
</body>
</html>
```